New travel store signage for our 2nd Mellow Journeys store to attract luxury travellers

Hello,

We had the attached signage created for our new branch but we are now looking to update our other branch to have new signage. This new sign must have the same colors and same design as the first graphic but it requires new information.

The top sign must include:
1. Sailing Beside Mellow Journeys Logo(attached)
2. The text...www.sailingbesidemellowjourneys.example
3. The text ... Specialists in Ocean, River, Exploration & Yacht-style Cruise Holidays
4. Brand Colours ( Fb0196, 412266, d41d84 and ffffff)

The bottom sign must include:
1. Mellow Journeys Outings Logo(attached)
2. The text...www.mellowjourneysoutings.example
3. The text ... Specialists in Day Trips, Theatre Trips, Short Breaks and More!

These new signs must match the design that was created in the first design and have the same colours and curve as your first design

Thank you

Target Market(s)

Retail

Industry/Entity Type

Travel Agency

Font styles to use
Other font styles liked:
• Radley

Colors
E54698
E96AAD
F1A4CE
F9D9EA
FCEFF6
A7469A
B969AE
D3A5CF
EDDBEB
F8F0F9

Requirements
Must have
• The top sign must include: 1. Sailing Beside Mellow Journeys Logo(attached) 2. The text...www.sailingbesidemellowjourneys.example 3. The text ... Specialists in Ocean, River, Exploration & Yacht-style Cruise Holidays 4. Brand Colours ( Fb0196, 412266, d41d84 and ffffff) The bottom sign must include: 1. Mellow Journeys Outings Logo(attached) 2. The text...www.mellowjourneysoutings.example 3. The text ... Specialists in Day Trips, Theatre Trips, Short Breaks and More! 4. Brand Colours ( Fb0196, 412266, d41d84 and ffffff)

```html
<!DOCTYPE html>
<html lang="en">
<head>
<meta charset="utf-8">
<title>Mellow Journeys – Shopfront Signage</title>
<link rel="stylesheet" href="https://fonts.googleapis.com/css2?family=Domine:wght@400;700&family=Open+Sans:wght@400&display=swap">
<style>
  :root {
    --brand-purple: #412266;
    --brand-pink: #fb0196;
    --brand-magenta: #d41d84;
    --brand-blush: #f1a4ce;
    --brand-white: #ffffff;
    --board-bg: #333333;
    --divider: #9a9a9a;
  }
  * { margin: 0; padding: 0; box-sizing: border-box; }
  html, body {
    width: 987px;
    height: 1200px;
    overflow: hidden;
    background: var(--board-bg);
  }
  .signage-board {
    width: 987px;
    height: 1200px;
    display: flex;
    flex-direction: column;
    align-items: center;
    justify-content: center;
    gap: 22px;
  }
  .sign-label {
    font-family: "Open Sans", sans-serif;
    font-size: 14px;
    color: var(--brand-white);
    letter-spacing: 0.2px;
  }
  .sign-label--bottom { margin-top: 30px; }
  .sign { display: block; }
  .sign--top { width: 773px; height: 63px; }
  .sign--bottom { width: 943px; height: 101px; }

  .fill-white { fill: var(--brand-white); }
  .fill-purple { fill: var(--brand-purple); }
  .panel-divider { stroke: var(--divider); stroke-width: 2; }

  .sign-url {
    font-family: "Domine", serif;
    font-weight: 400;
    fill: var(--brand-magenta);
  }
  .sign-tagline {
    font-family: "Domine", serif;
    font-weight: 700;
    fill: var(--brand-purple);
  }
  .sign-kicker {
    font-family: "Domine", serif;
    font-weight: 400;
    fill: var(--brand-magenta);
  }
  .sign-footer-url {
    font-family: "Domine", serif;
    font-weight: 400;
    fill: var(--brand-white);
  }
  .brand-name {
    font-family: "Domine", serif;
    font-weight: 700;
    fill: var(--brand-purple);
  }
</style>
</head>
<body>
<main class="signage-board">

  <p class="sign-label">Top Sign</p>

  <svg class="sign sign--top" viewBox="0 0 1288 105" role="img" aria-label="Top sign: Sailing Beside Mellow Journeys">
    <defs>
      <linearGradient id="edge-left" x1="0" y1="1" x2="1" y2="0">
        <stop offset="0" stop-color="#fb0196"/>
        <stop offset="1" stop-color="#f1a4ce"/>
      </linearGradient>
      <linearGradient id="edge-right" x1="1" y1="1" x2="0" y2="0">
        <stop offset="0" stop-color="#fb0196"/>
        <stop offset="1" stop-color="#f1a4ce"/>
      </linearGradient>
    </defs>
    <rect class="fill-purple" x="0" y="0" width="1288" height="105"/>
    <path fill="url(#edge-left)" d="M88 0 L644 0 L644 105 L0 105 Q4 14 88 0 Z"/>
    <path fill="url(#edge-right)" d="M644 0 L1180 0 Q1284 14 1288 105 L644 105 Z"/>
    <path class="fill-white" d="M100 0 L1168 0 Q1270 18 1276 105 L12 105 Q18 18 100 0 Z"/>

    <text class="brand-name" x="122" y="50" text-anchor="middle" font-size="19">Sailing Beside</text>
    <text class="brand-name" x="122" y="74" text-anchor="middle" font-size="19">Mellow Journeys</text>

    <text class="sign-url" x="644" y="50" text-anchor="middle" font-size="40" textLength="760" lengthAdjust="spacingAndGlyphs">www.sailingbesidemellowjourneys.example</text>
    <text class="sign-tagline" x="644" y="84" text-anchor="middle" font-size="22" textLength="822" lengthAdjust="spacingAndGlyphs">Specialists in Ocean, River, Exploration &amp; Yacht-style Cruise Holidays</text>

    <text class="brand-name" x="1160" y="50" text-anchor="middle" font-size="19">Sailing Beside</text>
    <text class="brand-name" x="1160" y="74" text-anchor="middle" font-size="19">Mellow Journeys</text>
  </svg>

  <p class="sign-label sign-label--bottom">Bottom Sign</p>

  <svg class="sign sign--bottom" viewBox="0 0 1572 169" role="img" aria-label="Bottom sign: Mellow Journeys Outings">
    <defs>
      <linearGradient id="stripe-main" x1="0" y1="0" x2="1" y2="0">
        <stop offset="0.35" stop-color="#fb0196"/>
        <stop offset="0.8" stop-color="#d41d84"/>
        <stop offset="1" stop-color="#f1a4ce"/>
      </linearGradient>
      <linearGradient id="stripe-side" x1="0" y1="0" x2="1" y2="0">
        <stop offset="0" stop-color="#f1a4ce"/>
        <stop offset="0.4" stop-color="#fb0196"/>
        <stop offset="1" stop-color="#d41d84"/>
      </linearGradient>
    </defs>

    <!-- main panel -->
    <rect class="fill-white" x="0" y="0" width="1181" height="169"/>
    <path fill="url(#stripe-main)" d="M0 139 C150 110 350 112 600 156 C820 168 1050 136 1181 70 L1181 169 L0 169 Z"/>
    <path class="fill-purple" d="M0 139 C150 110 350 112 600 162 C820 176 1050 150 1181 90 L1181 169 L0 169 Z"/>

    <text class="brand-name" x="291" y="70" text-anchor="middle" font-size="26">Mellow Journeys</text>
    <text class="brand-name" x="291" y="102" text-anchor="middle" font-size="26">Outings</text>

    <text class="sign-kicker" x="808" y="46" text-anchor="middle" font-size="29">Specialists in</text>
    <text class="sign-tagline" x="808" y="91" text-anchor="middle" font-size="31" textLength="590" lengthAdjust="spacingAndGlyphs">Day Trips, Theatre Trips, Short Breaks</text>
    <text class="sign-tagline" x="808" y="128" text-anchor="middle" font-size="31">and More!</text>

    <text class="sign-footer-url" x="127" y="156" font-size="18" textLength="330" lengthAdjust="spacingAndGlyphs">www.mellowjourneysoutings.example</text>

    <!-- return panel -->
    <rect class="fill-white" x="1181" y="0" width="391" height="169"/>
    <path fill="url(#stripe-side)" d="M1181 80 C1300 128 1450 148 1572 150 L1572 169 L1181 169 Z"/>
    <path class="fill-purple" d="M1181 96 C1300 140 1450 158 1572 160 L1572 169 L1181 169 Z"/>

    <text class="brand-name" x="1385" y="70" text-anchor="middle" font-size="26">Mellow Journeys</text>
    <text class="brand-name" x="1385" y="102" text-anchor="middle" font-size="26">Outings</text>

    <line class="panel-divider" x1="1181" y1="0" x2="1181" y2="169"/>
  </svg>

</main>
</body>
</html>
```